Female Vocalist with/Big Band Concert Marketing Package

Description

We would like to promote our Big Band Concert with a Nationally well known female Vocalist. She won the TV competition Fjellsang being Norways best artist of 2012 : http://www.kvorblad.no/scene/artikkel.php?artid=48213907

Size requirements :
Poster : A2 and A3
Flyer : 9x14 cm
Newspaper ad : Module 12B : 34 x 80 mm

Delivery file format :
PDFs in CMYK ready for printing
Must be editable in Illustrator CS6

Headlines :
Lene Holvik - main headline
m/Brekkvik Messingorkester - big band sharing the act
Messingkvelden - theme of this evening

Concert Dates, Venues and Web adresses :
27.april - Torvhaug Musikkhall - www.torvhaug-musikkhall.no
28.april - Brekkvik Kulturhus - www.brekkvik-kulturhus.no

Press Pictures and Graphics of artist and band :
May be used or not used according to design

Venue Logos :
There shall be a logo for each venue

Ticket sales logos :
There shall be a logo for each ticket sales office

Sponsors :
There must be a free field with room for sponsor logos

Link to graphics and logos :
https://www.filkassen.example/sh/q4lnzrwp8dyk2ha/mvTJ3uPq8x

```html
<!DOCTYPE html>
<html lang="no">
<head>
<meta charset="utf-8">
<title>Lene Holvik – Messingkvelden</title>
<link rel="stylesheet" href="https://fonts.googleapis.com/css2?family=Questrial&family=Crimson+Text:wght@400;600&family=Lato:wght@400;700&display=swap">
<style>
  :root {
    --page: #ffffff;
    --ink-black: #0a0603;
    --amber-deep: #5a2a05;
    --amber: #b8600f;
    --amber-bright: #f08a1c;
    --gold: #f6a33a;
    --silver-light: #f2f2f2;
    --silver-dark: #8d8d8d;
    --white: #ffffff;
    --venue-blue: #3a8fd0;
    --venue-green: #c8b41e;
  }
  html, body {
    margin: 0;
    padding: 0;
    width: 1200px;
    height: 542px;
    overflow: hidden;
    background: var(--page);
  }
  .banner {
    position: absolute;
    left: 34px;
    top: 32px;
    width: 1132px;
    height: 481px;
    overflow: hidden;
    background:
      radial-gradient(ellipse 420px 300px at 470px 200px, rgba(240,138,28,0.75), rgba(184,96,15,0.35) 55%, transparent 80%),
      linear-gradient(90deg, var(--ink-black) 0%, var(--amber-deep) 30%, var(--amber) 52%, var(--amber-deep) 75%, var(--ink-black) 100%);
  }
  .artist-photo {
    position: absolute;
    left: 614px;
    top: 0;
    width: 518px;
    height: 481px;
    background:
      radial-gradient(ellipse 230px 260px at 210px 190px, rgba(232,150,90,0.9), rgba(170,90,30,0.55) 60%, transparent 85%),
      linear-gradient(90deg, rgba(120,60,15,0) 0%, rgba(90,45,10,0.6) 40%, rgba(25,14,6,0.95) 100%);
  }
  .headline {
    position: absolute;
    left: 70px;
    top: 74px;
    margin: 0;
    font-family: "Questrial", sans-serif;
    font-weight: 400;
    font-size: 112px;
    letter-spacing: 1px;
    line-height: 1;
    color: var(--silver-light);
    background: linear-gradient(180deg, var(--silver-light) 0%, #c9c9c9 50%, var(--silver-dark) 100%);
    -webkit-background-clip: text;
    background-clip: text;
    -webkit-text-fill-color: transparent;
    -webkit-text-stroke: 1px rgba(60,60,60,0.6);
    filter: drop-shadow(2px 3px 3px rgba(0,0,0,0.6));
    white-space: nowrap;
  }
  .co-act {
    position: absolute;
    right: 548px;
    top: 190px;
    margin: 0;
    font-family: "Lato", sans-serif;
    font-size: 27px;
    color: var(--ink-black);
    white-space: nowrap;
  }
  .theme {
    position: absolute;
    left: 92px;
    top: 252px;
    margin: 0;
    font-family: "Crimson Text", serif;
    font-weight: 600;
    font-size: 80px;
    line-height: 1;
    background: linear-gradient(180deg, var(--gold) 0%, var(--amber-bright) 55%, #b85a0a 100%);
    -webkit-background-clip: text;
    background-clip: text;
    -webkit-text-fill-color: transparent;
    filter: drop-shadow(2px 3px 3px rgba(0,0,0,0.7));
    white-space: nowrap;
  }
  .dates {
    position: absolute;
    left: 98px;
    top: 386px;
    display: flex;
    gap: 22px;
  }
  .date {
    display: flex;
    gap: 8px;
  }
  .venue-badge {
    width: 36px;
    height: 44px;
    flex: none;
  }
  .venue-badge.first { background: var(--venue-blue); }
  .venue-badge.second { background: var(--venue-green); }
  .date-text {
    font-family: "Lato", sans-serif;
    line-height: 1.25;
  }
  .date-line {
    display: block;
    font-size: 19px;
    color: var(--white);
    white-space: nowrap;
  }
  .date-url {
    display: block;
    padding-left: 14px;
    font-size: 19px;
    color: var(--gold);
    white-space: nowrap;
  }
  .tickets {
    position: absolute;
    left: 960px;
    top: 380px;
    font-family: "Lato", sans-serif;
    color: var(--white);
  }
  .tickets-label {
    font-size: 15px;
    margin: 0 0 10px;
  }
  .ticket-offices {
    display: flex;
    gap: 8px;
    align-items: center;
  }
  .ticket-office {
    font-size: 12px;
    font-weight: 700;
    color: var(--white);
  }
  .ticket-office.boxed {
    background: var(--white);
    color: var(--ink-black);
    padding: 8px 5px;
  }
</style>
</head>
<body>
  <main class="banner">
    <div class="artist-photo" role="img" aria-label="Press photo of the vocalist smiling, with saxophone and trombone player of the big band"></div>

    <h1 class="headline">Lene Holvik</h1>
    <p class="co-act">m/Brekkvik Messingorkester</p>
    <h2 class="theme">Messingkvelden</h2>

    <section class="dates">
      <div class="date">
        <div class="venue-badge first" aria-hidden="true"></div>
        <div class="date-text">
          <span class="date-line">27.april - Torvhaug Musikkhall</span>
          <span class="date-url">www.torvhaug-musikkhall.no</span>
        </div>
      </div>
      <div class="date">
        <div class="venue-badge second" aria-hidden="true"></div>
        <div class="date-text">
          <span class="date-line">28.april - Brekkvik Kulturhus</span>
          <span class="date-url">www.brekkvik-kulturhus.no</span>
        </div>
      </div>
    </section>

    <section class="tickets">
      <p class="tickets-label">tickets available at:</p>
      <div class="ticket-offices">
        <span class="ticket-office">Billettnett</span>
        <span class="ticket-office boxed">Billettkontoret</span>
      </div>
    </section>
  </main>
</body>
</html>
```